New Business Card Design Project - Moreland Bookkeeping & Tax Services, LLC

Below is a sample image of the card (Fenwick Ledger). I would like to have a designed business card that looks very similar (Front & Back). In addition, I would like to keep the same colors as well. I attached my Business Logo (Moreland Bookkeeping & Tax Services, LLC) that will be on my website.

Target Market(s)

Executives, Business Owners, Board of Directors, Chief Financial Officers

Contact Information for Business Card

Font styles to use
Serif

Colors
0c5ba6
ffffff
5c5c5c

Requirements
Must have
• My Name: Calvin Prewitt, CPA
• Position: Owner
• Phone: (555) 555-0148
• Email: Cprewitt@morelandbooks.com
• Website: www.Morelandbooks.com
• Address: 42917 Birch Hollow Dr #2306
• Harlow Glen, ST 21190
Nice to have
• Same design & color scheme as Fenwick Ledgr Business card sample attached

```html
<!DOCTYPE html>
<html lang="en">
<head>
<meta charset="utf-8">
<title>Moreland Bookkeeping &amp; Tax Services – Business Card</title>
<link rel="stylesheet" href="https://fonts.googleapis.com/css2?family=Tinos:wght@400;700&display=swap">
<style>
  :root {
    --brand-blue: #0c5ba6;
    --deep-blue: #0b2a66;
    --ink: #1f1f1f;
    --grey: #5c5c5c;
    --card: #f3f3f2;
    --backdrop: #d9d6d1;
  }
  * { box-sizing: border-box; margin: 0; padding: 0; }
  html, body {
    width: 1200px; height: 970px; overflow: hidden;
    background: var(--backdrop);
  }
  .business-card {
    position: absolute; left: 182px; top: 270px;
    width: 834px; height: 475px;
    background: linear-gradient(160deg, #fbfbfa 0%, var(--card) 60%, #ecebe9 100%);
    box-shadow: 0 12px 32px rgba(0,0,0,.18);
    overflow: hidden;
    font-family: "Tinos", "Times New Roman", serif;
  }
  .brand-block {
    position: absolute; left: 34px; top: 198px; width: 380px;
    display: flex; flex-direction: column; align-items: center; gap: 62px;
  }
  .brand-dot {
    width: 20px; height: 20px; border-radius: 50%;
    background: var(--brand-blue);
  }
  .brand-name {
    color: var(--brand-blue); font-weight: 400;
    font-size: 17px; letter-spacing: 2px; text-transform: uppercase;
    text-align: center; line-height: 1.45;
  }
  .divider {
    position: absolute; left: 410px; top: 142px;
    width: 2px; height: 189px; background: var(--deep-blue);
  }
  .contact-block { position: absolute; left: 453px; top: 138px; color: var(--ink); }
  .person-name { font-size: 24px; font-weight: 400; line-height: 1; }
  .person-role { font-size: 19px; color: var(--deep-blue); line-height: 1; margin-top: 1px; }
  .address { font-size: 20px; line-height: 26px; margin-top: 14px; }
  .contact-list { list-style: none; margin-top: 10px; font-size: 20px; }
  .contact-list li { display: flex; align-items: center; gap: 10px; height: 26px; }
  .contact-list svg { width: 17px; height: 17px; fill: var(--deep-blue); flex: none; }
  .band { position: absolute; bottom: 0; }
  .band-grey { left: 0; width: 472px; height: 26px; }
  .band-blue { right: 0; width: 360px; height: 46px; }
</style>
</head>
<body>
  <main class="business-card">
    <section class="brand-block">
      <span class="brand-dot"></span>
      <p class="brand-name">Moreland Bookkeeping<br>&amp; Tax Services, LLC</p>
    </section>

    <span class="divider"></span>

    <section class="contact-block">
      <h1 class="person-name">Calvin Prewitt, CPA</h1>
      <p class="person-role">Owner</p>
      <p class="address">42917 Birch Hollow Dr #2306<br>Harlow Glen, ST 21190</p>
      <ul class="contact-list">
        <li>
          <svg viewBox="0 0 24 24" aria-hidden="true"><path d="M3 8c0-3 4-4 9-4s9 1 9 4v2h-5V8H8v2H3zM6 11h12l2 8H4z"/></svg>
          (555) 555-0148
        </li>
        <li>
          <svg viewBox="0 0 24 24" aria-hidden="true"><path d="M2 6h20v12H2zM3.5 7.5 12 13l8.5-5.5" stroke="#fff" stroke-width="1.5"/></svg>
          Cprewitt@morelandbooks.com
        </li>
        <li>
          <svg viewBox="0 0 24 24" aria-hidden="true"><circle cx="12" cy="12" r="10"/><path d="M2 12h20M12 2c4 4 4 16 0 20M12 2c-4 4-4 16 0 20" stroke="#fff" stroke-width="1.3" fill="none"/></svg>
          www.Morelandbooks.com
        </li>
      </ul>
    </section>

    <svg class="band band-grey" viewBox="0 0 472 26" preserveAspectRatio="none" aria-hidden="true">
      <defs><linearGradient id="greyBand" x1="0" x2="1"><stop offset="0" stop-color="#2c2c2c"/><stop offset="1" stop-color="#5c5c5c"/></linearGradient></defs>
      <polygon points="0,0 472,0 464,26 0,26" fill="url(#greyBand)"/>
    </svg>
    <svg class="band band-blue" viewBox="0 0 360 46" preserveAspectRatio="none" aria-hidden="true">
      <defs><linearGradient id="blueBand" x1="0" x2="1"><stop offset="0" stop-color="#081c48"/><stop offset="1" stop-color="#0b2a66"/></linearGradient></defs>
      <polygon points="10,0 360,0 360,46 0,46" fill="url(#blueBand)"/>
    </svg>
  </main>
</body>
</html>
```